PTA Meeting Poster

We are looking to create a poster to invite parents of our school to our monthly PTA Meeting.

The copy should include:

PTA Meeting
This Wednesday
8:40am
in the Multi Purpose Room

All Welcome!

```html
<!DOCTYPE html>
<html lang="en">
<head>
<meta charset="utf-8">
<title>PTA Meeting Poster</title>
<link rel="stylesheet" href="https://fonts.googleapis.com/css2?family=Arimo:wght@400;700&family=Source+Sans+3:wght@400;600&display=swap">
<style>
  :root {
    --paper: #ffffff;
    --device: #141414;
    --device-edge: #3a3a3a;
    --screen: #f4f5f7;
    --bar-top: #b9c8dc;
    --bar-bottom: #6f8bb0;
    --header-top: #f7f8fa;
    --header-bottom: #d9dde3;
    --heading-ink: #2f3e55;
    --grid-line: #d5d8dd;
    --time-ink: #7b7f86;
    --event-fill: #bfe6fb;
    --event-edge: #7cc4ea;
    --event-ink: #1f6fd6;
    --bubble-green: #9cf01e;
    --bubble-green-edge: #6fb20c;
    --bubble-grey: #cfcfcf;
    --bubble-grey-edge: #9a9a9a;
    --ink: #111111;
  }
  html, body {
    margin: 0;
    padding: 0;
    overflow: hidden;
    background: var(--paper);
  }
  .poster {
    width: 848px;
    height: 1200px;
    position: relative;
    overflow: hidden;
    background: var(--paper);
  }
  .poster svg { display: block; }
  .ui-text { font-family: "Arimo", "Helvetica Neue", Arial, sans-serif; }
  .bubble-text { font-family: "Source Sans 3", "Myriad Pro", Arial, sans-serif; fill: var(--ink); }
  .time-label { font-size: 21px; fill: var(--time-ink); }
  .nav-heading { font-size: 34px; font-weight: 700; fill: var(--heading-ink); }
  .bar-title { font-size: 30px; font-weight: 700; fill: #ffffff; }
  .bar-button { font-size: 19px; font-weight: 700; fill: #ffffff; }
  .event-title { font-size: 20px; font-weight: 700; fill: var(--event-ink); }
  .event-place { font-size: 20px; fill: var(--event-ink); }
  .banner-title { font-size: 50px; font-weight: 700; fill: var(--event-ink); }
  .banner-place { font-size: 46px; fill: var(--event-ink); }
</style>
</head>
<body>
<main class="poster">
  <svg width="848" height="1200" viewBox="0 0 848 1200" xmlns="http://www.w3.org/2000/svg">
    <defs>
      <linearGradient id="navBar" x1="0" y1="0" x2="0" y2="1">
        <stop offset="0" stop-color="var(--bar-top)"/>
        <stop offset="1" stop-color="var(--bar-bottom)"/>
      </linearGradient>
      <linearGradient id="dayHeader" x1="0" y1="0" x2="0" y2="1">
        <stop offset="0" stop-color="var(--header-top)"/>
        <stop offset="1" stop-color="var(--header-bottom)"/>
      </linearGradient>
      <linearGradient id="greenBubble" x1="0" y1="0" x2="0" y2="1">
        <stop offset="0" stop-color="#b8ff4a"/>
        <stop offset="1" stop-color="var(--bubble-green)"/>
      </linearGradient>
      <linearGradient id="greyBubble" x1="0" y1="0" x2="0" y2="1">
        <stop offset="0" stop-color="#e6e6e6"/>
        <stop offset="1" stop-color="var(--bubble-grey)"/>
      </linearGradient>
    </defs>

    <!-- Handset -->
    <g class="handset" transform="rotate(-5 430 620)">
      <rect class="handset-body" role="img" aria-label="Black smartphone holding the calendar"
            x="40" y="-40" width="790" height="1290" rx="110" fill="var(--device)" stroke="var(--device-edge)" stroke-width="6"/>

      <!-- Calendar screen -->
      <g class="calendar-screen ui-text">
        <rect x="95" y="200" width="680" height="870" fill="var(--screen)"/>
        <rect class="status-bar" x="95" y="200" width="680" height="32" fill="#8ea6c6"/>
        <text x="140" y="224" class="bar-button">PTA</text>
        <rect class="nav-bar" x="95" y="232" width="680" height="72" fill="url(#navBar)"/>
        <rect x="108" y="246" width="130" height="44" rx="8" fill="#5d7aa3" stroke="#42608a"/>
        <text x="173" y="275" text-anchor="middle" class="bar-button">Calendars</text>
        <text x="440" y="280" text-anchor="middle" class="bar-title">Calendars</text>
        <rect x="700" y="220" width="60" height="44" rx="8" fill="#3f6fc0"/>
        <rect class="day-header" x="95" y="304" width="680" height="72" fill="url(#dayHeader)"/>
        <text x="440" y="352" text-anchor="middle" class="nav-heading">This Wednesday</text>
        <path d="M140 352 l16 -10 v20 z M740 342 l16 10 -16 10 z" fill="var(--heading-ink)"/>

        <g class="hour-grid" stroke="var(--grid-line)" stroke-width="2">
          <line x1="215" y1="428" x2="760" y2="428"/>
          <line x1="215" y1="503" x2="760" y2="503"/>
          <line x1="215" y1="578" x2="760" y2="578"/>
          <line x1="215" y1="728" x2="760" y2="728"/>
          <line x1="215" y1="803" x2="760" y2="803"/>
          <line x1="215" y1="878" x2="760" y2="878"/>
        </g>
        <text x="125" y="436" class="time-label">08:00</text>
        <text x="125" y="511" class="time-label">09:00</text>
        <text x="125" y="811" class="time-label">13:00</text>

        <rect class="event-block" x="225" y="446" width="450" height="92" rx="8" fill="var(--event-fill)" stroke="var(--event-edge)" stroke-width="2"/>
        <text x="238" y="474" class="event-title">PTA Meeting</text>
        <text x="238" y="500" class="event-place">Multi-purpose room</text>

        <rect class="tab-bar" x="95" y="990" width="680" height="80" fill="url(#navBar)"/>
        <rect x="545" y="1004" width="100" height="46" rx="8" fill="#5d7aa3"/>
        <text x="595" y="1034" text-anchor="middle" class="bar-button">Month</text>
        <rect x="665" y="1004" width="90" height="46" rx="8" fill="#3f6fc0"/>
        <path d="M710 1014 v18 m-8 -8 l8 8 8 -8 M696 1034 v8 h28 v-8" fill="none" stroke="#ffffff" stroke-width="3"/>
      </g>
      <circle class="home-button" cx="500" cy="1160" r="40" fill="none" stroke="var(--device-edge)" stroke-width="5"/>
    </g>

    <!-- Headline bubble -->
    <g class="headline-bubble">
      <path d="M320 48 H808 a18 18 0 0 1 18 18 V200 a18 18 0 0 1 -18 18 H320 a18 18 0 0 1 -18 -18 V66 a18 18 0 0 1 18 -18 Z M800 214 q20 2 26 4 q-14 -2 -26 -20 Z"
            fill="url(#greenBubble)" stroke="var(--bubble-green-edge)" stroke-width="2"/>
      <text x="328" y="160" class="bubble-text" font-size="76">PARENTS!</text>
    </g>

    <!-- Enlarged meeting banner -->
    <g class="meeting-banner ui-text" transform="rotate(-5 424 660)">
      <rect x="-20" y="585" width="890" height="150" rx="10" fill="var(--event-fill)" stroke="var(--event-edge)" stroke-width="3"/>
      <text x="32" y="655" class="banner-title">PTA Meeting <tspan dx="18">08:40</tspan></text>
      <text x="32" y="712" class="banner-place">Multi-purpose room</text>
    </g>

    <!-- Welcome bubble -->
    <g class="welcome-bubble">
      <path d="M72 855 H528 a18 18 0 0 1 18 18 V1004 a18 18 0 0 1 -18 18 H72 a18 18 0 0 1 -18 -18 V873 a18 18 0 0 1 18 -18 Z M58 1000 q-14 16 -28 22 q18 0 38 -8 Z"
            fill="url(#greyBubble)" stroke="var(--bubble-grey-edge)" stroke-width="2"/>
      <text x="66" y="945" class="bubble-text" font-size="56">ALL Welcome.</text>
    </g>
  </svg>
</main>
</body>
</html>
```